Business card design for niche B2B media co.

Looking for a sophisticated business card that captures our recent redesign. We are a media business with two publications that also runs conferences for the banking industry in Australia/NZ.

The slogan we have started using is:

Read. Share. Connect. Innovate.

Our strategic purpose is to help the financial services industry deliver a better banking experience to customers across all distribution channels.

We do this by providing compelling content and bringing our audience together to share knowledge.

We would like a two sided card, but other than that we're not precious about the type of design.

Target Market(s)

Bankers and vendors that serve the banking industry

Industry/Entity Type

Business

Requirements
Must have
• Ledger Crest Media Logo, Name (Delia Okafor), job title (Editor), Phone/fax numbers +61 7 3894 5106, + 61 7 3894 5681 , email address (dokafor@webledgercrest.com.au), skype address (delia.okafor), website address www.ledgercrest.com.au, twitter tag @ledgercrest, slogan as detailed above
Nice to have
• Other logos - we have a logo for Ledger Crest Conferences and also the two mastheads Web Ledger Crest & Counter Ledger Crest
Should not have
• stock photos - yuck!

```html
<!DOCTYPE html>
<html lang="en">
<head>
<meta charset="utf-8">
<title>Ledger Crest Media – Business Card</title>
<link rel="stylesheet" href="https://fonts.googleapis.com/css2?family=Arimo:wght@400;700&family=Nunito:wght@800&display=swap">
<style>
  :root {
    --stage: #3a3a3c;
    --card: #ffffff;
    --blue: #0679c4;
    --blue-deep: #0566a8;
    --ink: #1c1c22;
    --grey: #8f9194;
  }
  * { box-sizing: border-box; margin: 0; padding: 0; }
  html, body { width: 1200px; height: 750px; overflow: hidden; }
  body { background: var(--stage); position: relative; font-family: "Arimo", Arial, sans-serif; }

  .card {
    position: absolute; width: 536px; height: 306px;
    background: var(--card); border-radius: 22px; overflow: hidden;
    box-shadow: 0 14px 30px rgba(0,0,0,.45);
  }
  .card--front { left: 83px; top: 62px; }
  .card--back { left: 542px; top: 377px; }

  .wave { position: absolute; inset: 0; width: 100%; height: 100%; }

  .tagline {
    position: absolute; font-family: "Nunito", Verdana, sans-serif; font-weight: 800;
    color: var(--grey); font-size: 17.5px; letter-spacing: .3px; white-space: nowrap;
  }
  .card--front .tagline { left: 213px; top: 44px; }
  .card--back .tagline { left: 0; right: 0; top: 40px; text-align: center; }

  .brand { position: absolute; font-weight: 700; color: var(--ink); line-height: 1.05; white-space: nowrap; }

  .card--front .brand--main { left: 31px; top: 40px; font-size: 24px; }
  .card--front .brand--web { left: 19px; top: 118px; font-size: 12px; }
  .card--front .brand--conf { left: 104px; top: 118px; font-size: 12px; }
  .card--front .brand--counter { left: 55px; top: 156px; font-size: 12px; }

  .card--back .brand--main { left: 190px; top: 84px; font-size: 32px; }
  .card--back .brand--counter { left: 37px; top: 146px; font-size: 21px; }
  .card--back .brand--conf { left: 357px; top: 146px; font-size: 21px; }
  .card--back .brand--web { left: 193px; top: 200px; font-size: 23px; }

  .website { position: absolute; left: 0; right: 0; top: 270px; text-align: center; color: var(--grey); font-size: 15px; letter-spacing: .5px; }

  .holder { position: absolute; right: 48px; top: 138px; text-align: right; color: #fff; }
  .holder__name { font-weight: 700; font-size: 35px; line-height: 1; }
  .holder__role { font-size: 23px; letter-spacing: 2px; line-height: 1.05; }

  .contact { position: absolute; left: 44px; top: 214px; color: #fff; font-size: 18.5px; line-height: 22px; letter-spacing: .6px; }
  .lines { position: absolute; left: 312px; top: 236px; color: #fff; font-weight: 700; font-size: 18.5px; line-height: 22px; letter-spacing: .8px; }
  .lines dt { float: left; width: 46px; }
  .lines dd { margin-left: 46px; }
</style>
</head>
<body>

<section class="card card--front" aria-label="Business card front">
  <svg class="wave" viewBox="0 0 536 306" preserveAspectRatio="none" aria-hidden="true">
    <path d="M0 185 C40 205 90 210 150 190 C230 160 290 85 375 83 C440 82 500 115 536 147 L536 306 L0 306 Z" fill="var(--blue)"/>
    <path d="M0 200 C60 250 140 260 220 220 C300 180 380 120 536 160 L536 150 C500 118 440 95 380 98 C300 100 240 175 160 205 C100 225 40 215 0 190 Z" fill="var(--blue-deep)" opacity=".6"/>
  </svg>

  <p class="brand brand--main">Ledger Crest<br>Media</p>
  <p class="tagline">Read. Share. Connect. Innovate.</p>
  <p class="brand brand--web">Web<br>Ledger Crest</p>
  <p class="brand brand--conf">Ledger Crest<br>Conferences</p>
  <p class="brand brand--counter">Counter<br>Ledger Crest</p>

  <div class="holder">
    <p class="holder__name">Delia Okafor</p>
    <p class="holder__role">Editor</p>
  </div>

  <p class="contact">
    Email dokafor@webledgercrest.com.au<br>
    Skype delia.okafor<br>
    Twitter Tag @ledgercrest
  </p>
  <dl class="lines">
    <dt>Ph</dt><dd>61 7 3894 5106</dd>
    <dt>Fax</dt><dd>61 7 3894 5681</dd>
  </dl>
</section>

<section class="card card--back" aria-label="Business card back">
  <p class="tagline">Read. Share. Connect. Innovate.</p>
  <p class="brand brand--main">Ledger Crest<br>Media</p>
  <p class="brand brand--counter">Counter<br>Ledger Crest</p>
  <p class="brand brand--conf">Ledger Crest<br>Conferences</p>
  <p class="brand brand--web">Web<br>Ledger Crest</p>
  <p class="website">www.ledgercrest.com.au</p>
</section>

</body>
</html>
```